New Tech Support Service needs a website design

We need a web design for a new product we are developing that provides tech support to consumers for a small ongoing monthly fee. We are looking for a fresh, technology look and feel. We want the site to have a tech feel - yet not intimidating. Simple and welcoming. We are in need of an initial landing page, sign on page, and a product home page.

Thank you to everyone who submitted designs. It was a very difficult decision!

Industry/Entity Type

Tech

```html
<!DOCTYPE html>
<html lang="en">
<head>
<meta charset="utf-8">
<title>Company Name – PC Support</title>
<link rel="stylesheet" href="https://fonts.googleapis.com/css2?family=Open+Sans:wght@400;600;700&family=Oswald:wght@400;500;600&display=swap">
<style>
:root{
  --blue:#1c4ea3;
  --blue-deep:#0d3f8f;
  --blue-bright:#1a8fd6;
  --green:#7dbb2f;
  --green-text:#8fc63c;
  --dark:#222;
  --darker:#1b1b1b;
  --ink:#333;
  --muted:#777;
  --light:#f2f2f2;
  --line:#dcdcdc;
  --white:#fff;
}
*{box-sizing:border-box;margin:0;padding:0}
html,body{width:764px;height:1200px;overflow:hidden}
body{position:relative;background:var(--white);font-family:"Open Sans",Arial,sans-serif;color:var(--ink)}
.abs{position:absolute}
.cond{font-family:"Oswald","Arial Narrow",sans-serif}

/* top bar */
.topbar{left:0;top:0;width:764px;height:21px;background:var(--blue)}
.topbar ul{list-style:none;position:absolute;right:118px;top:0;display:flex;gap:14px;height:21px;align-items:center}
.topbar li{font-size:7px;color:var(--white);display:flex;align-items:center;gap:4px;letter-spacing:.3px}
.topbar li span.dot{width:7px;height:7px;background:var(--white);border-radius:1px;display:inline-block}

/* header */
.brand{left:128px;top:28px;font-size:25px;color:var(--blue-deep);font-weight:400}
.brand b{font-weight:400}
.nav{right:124px;top:34px;display:flex;gap:22px}
.nav a{display:flex;flex-direction:column;align-items:center;font-family:"Oswald",sans-serif;font-size:10px;color:#555;text-decoration:none;gap:3px}
.nav a svg{width:12px;height:12px}
.nav a.active{color:var(--blue-deep);border-bottom:2px solid var(--blue-deep);padding-bottom:2px}

/* hero */
.hero{left:0;top:83px;width:764px;height:245px;background:linear-gradient(180deg,#ffffff 0%,#e4f1fb 60%,#d3e8f7 100%)}
.hero-title{left:121px;top:121px;font-size:29px;font-weight:700;color:var(--blue-deep);letter-spacing:1px}
.hero-sub{left:121px;top:158px;font-size:21px;color:var(--ink);letter-spacing:.5px}
.hero-text{left:121px;top:196px;width:240px;font-size:8px;line-height:13px;color:#555}
.btn-plans{left:120px;top:237px;width:128px;height:27px;background:var(--blue-deep);color:var(--white);font-size:9.5px;display:flex;align-items:center;justify-content:center;gap:6px;clip-path:polygon(0 0,92% 0,100% 50%,92% 100%,0 100%)}
.hero-art{left:410px;top:93px;width:230px;height:214px;border-radius:8px;background:radial-gradient(circle at 45% 45%,#7fc3f0 0%,#3f6d95 45%,#2a2f36 75%,transparent 76%)}
.slide-arrow{width:16px;height:16px;border-radius:50%;background:var(--blue-bright);top:179px}

/* tagline band */
.band{left:0;top:328px;width:764px;height:56px;background:var(--dark);display:flex;align-items:center;justify-content:center;font-size:15px;color:var(--white);letter-spacing:1.5px}
.band em,.footband em{font-style:normal;color:var(--green-text)}

/* section headings */
.h-sec{font-family:"Oswald",sans-serif;font-size:13.5px;color:#222;letter-spacing:.3px}

/* computer problem panel */
.problem{left:120px;top:429px;width:380px;height:147px;background:#e9e9e9}
.who{left:120px;top:429px;width:184px;height:147px;background:var(--blue)}
.who h3{position:absolute;left:14px;top:24px;font-family:"Oswald",sans-serif;font-size:11px;color:var(--white)}
.who p{position:absolute;left:14px;top:42px;width:80px;font-size:6.5px;line-height:10px;color:#dce6f7}
.who .more{position:absolute;left:14px;top:95px;width:68px;height:20px;background:var(--blue-deep);border:1px solid #4f7fcf;font-family:"Oswald",sans-serif;font-size:9px;color:var(--white);display:flex;align-items:center;justify-content:center;gap:4px}
.who-photo{left:222px;top:429px;width:82px;height:147px;background:linear-gradient(180deg,#3a5fa8,#1a1a1a 70%)}
.tool{width:79px;height:57px;background:var(--white);border:1px solid #ccc;display:flex;flex-direction:column;align-items:center;justify-content:center;gap:4px}
.tool svg{width:13px;height:13px}
.tool .name{font-size:6.5px;color:#444}
.tool .dl{font-family:"Oswald",sans-serif;font-size:7px;color:var(--blue-deep)}

/* hot offer */
.offer{left:513px;top:429px;width:130px;height:147px;border:1px solid #ddd;background:var(--white);overflow:hidden}
.offer .ribbon{position:absolute;right:-22px;top:10px;width:80px;height:12px;background:#222;color:var(--white);font-size:5px;text-align:center;line-height:12px;transform:rotate(45deg)}
.offer .t{position:absolute;left:0;top:40px;width:100%;text-align:center;font-family:"Oswald",sans-serif;font-size:9px;line-height:12px;color:#222}
.offer .price{position:absolute;left:0;top:70px;width:100%;text-align:center;font-family:"Oswald",sans-serif;font-size:19px;color:var(--blue-deep)}
.offer .price small{font-size:9px;color:#999}
.offer .boxes{position:absolute;left:22px;top:107px;width:86px;height:20px;background:linear-gradient(180deg,#f4f4f4,#dedede)}

/* features */
.features{left:0;top:600px;width:764px;height:233px;background:#eeeeee}
.feature{top:637px;width:164px;height:166px;background:var(--white);border-top:3px solid var(--blue);box-shadow:0 1px 3px rgba(0,0,0,.12)}
.feature .badge{position:absolute;left:0;top:0;width:49px;height:48px;background:var(--blue);clip-path:polygon(0 0,100% 0,100% 75%,50% 100%,0 75%);color:var(--white);font-size:24px;display:flex;align-items:flex-start;justify-content:center;padding-top:4px}
.feature h4{position:absolute;left:58px;top:10px;font-family:"Oswald",sans-serif;font-size:13px;font-weight:400;color:#222}
.feature .sub{position:absolute;left:58px;top:31px;font-size:7px;color:#666}
.feature .dots{position:absolute;left:0;top:56px;width:100%;text-align:center;color:#ccc;font-size:8px;letter-spacing:2px}
.feature p{position:absolute;left:10px;top:72px;width:144px;font-size:6.5px;line-height:11px;color:#777;text-align:center}
.feature .more{position:absolute;left:37px;top:124px;width:90px;height:21px;background:#333;color:var(--white);font-family:"Oswald",sans-serif;font-size:9.5px;display:flex;align-items:center;justify-content:center;border-radius:2px}

/* service plan */
.rule{height:2px;background:var(--blue)}
.plan{width:76px;height:39px;border:1px solid #ddd;background:var(--white);display:flex;align-items:center;gap:6px;padding-left:6px}
.plan .n{width:21px;height:21px;border-radius:50%;border:1px solid #ccc;background:#f4f4f4;font-size:10px;color:#888;display:flex;align-items:center;justify-content:center}
.plan .l{font-size:8.5px;line-height:12px;color:#333}
.whatwedo{left:396px;top:891px;width:248px;height:89px;border:1px solid #ddd;background:#fafafa}
.wwd-photo{left:413px;top:906px;width:67px;height:54px;background:linear-gradient(180deg,#dfe7ef,#6c7a88)}
.wwd-text{left:490px;top:904px;width:145px;font-size:6.5px;line-height:11px;color:#666;text-align:justify}
.wwd-more{left:608px;top:959px;font-size:7px;font-weight:700;color:#222}

/* footer */
.footband{left:0;top:1031px;width:764px;height:36px;background:var(--darker);display:flex;align-items:center;padding-left:125px;font-family:"Oswald",sans-serif;font-size:13.5px;color:var(--white);letter-spacing:.5px}
.callbox{left:440px;top:1014px;width:324px;height:53px;background:var(--green);clip-path:polygon(14% 32%,100% 0,100% 100%,0 100%)}
.call{left:476px;top:1039px;display:flex;align-items:center;gap:6px;font-family:"Oswald",sans-serif;font-size:14px;color:var(--white)}
.call .c{width:11px;height:11px;border-radius:50%;background:#e8e8e8}
.footer{left:0;top:1067px;width:764px;height:133px;background:#2a2a2a}
.f-h{font-family:"Oswald",sans-serif;font-size:10.5px;color:var(--white)}
.f-list{list-style:none}
.f-list li{font-size:6px;color:#aaa;line-height:14px;letter-spacing:.3px}
.f-list li::before{content:"›";color:#ddd;margin-right:5px}
.f-about{left:433px;top:1112px;width:206px;font-size:6px;line-height:13px;color:#999}
</style>
</head>
<body>

<div class="abs topbar">
  <ul>
    <li><span class="dot"></span>LIVE CHAT</li>
    <li><span class="dot"></span>COMMUNITY</li>
    <li><span class="dot"></span>UPDATES</li>
    <li><span class="dot"></span>NEWSFEED</li>
  </ul>
</div>

<div class="abs brand">Company <b style="color:#222">Name</b></div>
<nav class="abs nav">
  <a class="active" href="#"><svg viewBox="0 0 12 12"><path d="M1 6 6 1l5 5H9.5v5h-7V6z" fill="#555"/></svg>HOME</a>
  <a href="#"><svg viewBox="0 0 12 12"><rect x="2" y="3" width="8" height="7" fill="#555"/><rect x="4" y="1" width="4" height="3" fill="none" stroke="#555"/></svg>ABOUT US</a>
  <a href="#"><svg viewBox="0 0 12 12"><path d="M1 6a5 5 0 0 1 10 0z" fill="#555"/><path d="M6 6v4a1 1 0 0 1-2 0" stroke="#555" fill="none"/></svg>SERVICE PLAN</a>
  <a href="#"><svg viewBox="0 0 12 12"><path d="M2 7a4 4 0 0 1 8 0" stroke="#555" fill="none" stroke-width="1.5"/><rect x="1" y="6" width="2.5" height="4" fill="#555"/><rect x="8.5" y="6" width="2.5" height="4" fill="#555"/></svg>CONTACT</a>
</nav>

<section class="abs hero"></section>
<div class="abs hero-art" role="img" aria-label="Desktop computer tower with a monitor showing a blue screen"></div>
<div class="abs slide-arrow" style="left:77px"><svg viewBox="0 0 16 16" width="16" height="16"><path d="M9.5 5 6.5 8l3 3" stroke="#fff" stroke-width="1.6" fill="none"/></svg></div>
<div class="abs slide-arrow" style="left:650px"><svg viewBox="0 0 16 16" width="16" height="16"><path d="M6.5 5l3 3-3 3" stroke="#fff" stroke-width="1.6" fill="none"/></svg></div>
<h1 class="abs hero-title cond" style="font-weight:600">FIX YOUR</h1>
<h2 class="abs hero-sub cond" style="font-weight:400">PC PROBLEM NOW</h2>
<p class="abs hero-text">Our optimization service involves removal of your pc threats, unwanted files and unnecessary background processes.</p>
<a class="abs btn-plans cond">VIEW PLANS &amp; FEATURES <span>»</span></a>

<div class="abs band cond">PC OPTIMIZE TOOL FOR&nbsp;<em>SUPPORT &amp; SPEED</em>&nbsp;UP YOUR PC</div>

<h3 class="abs h-sec" style="left:120px;top:405px">COMPUTER PROBLEM ?</h3>
<h3 class="abs h-sec" style="left:513px;top:405px">HOT OFFER</h3>

<div class="abs problem"></div>
<div class="abs who">
  <h3>WHO WE ARE</h3>
  <p>fixmydesk.com is a technical support service covering the World. As computers have become .....</p>
  <div class="more">READ MORE <span>›</span></div>
</div>
<div class="abs who-photo" role="img" aria-label="Support agent giving a thumbs up"></div>

<div class="abs tool" style="left:316px;top:441px">
  <svg viewBox="0 0 13 13"><path d="M2 11 8 5M3 2l8 8M9 1l3 3-2 2-3-3z" stroke="#333" stroke-width="1.6" fill="none"/></svg>
  <span class="name">Remote Support RSA</span><span class="dl">DOWNLOAD</span>
</div>
<div class="abs tool" style="left:407px;top:441px">
  <svg viewBox="0 0 13 13"><circle cx="6.5" cy="6.5" r="5" stroke="#333" stroke-width="1.5" fill="none"/><path d="M6.5 6.5 9 4" stroke="#333" stroke-width="1.5"/></svg>
  <span class="name">Remote Support RSB</span><span class="dl">DOWNLOAD</span>
</div>
<div class="abs tool" style="left:316px;top:507px">
  <svg viewBox="0 0 13 13"><circle cx="6.5" cy="6.5" r="5" stroke="#333" stroke-width="1.5" fill="none"/><path d="M6.5 3v3.5h2.5" stroke="#333" stroke-width="1.5" fill="none"/></svg>
  <span class="name">Remote Support RSC</span><span class="dl">DOWNLOAD</span>
</div>
<div class="abs tool" style="left:407px;top:507px">
  <svg viewBox="0 0 13 13"><circle cx="5" cy="6" r="3" stroke="#333" stroke-width="2" fill="none"/><circle cx="10" cy="10" r="2" stroke="#333" stroke-width="1.5" fill="none"/></svg>
  <span class="name">Remote Support RSD</span><span class="dl">DOWNLOAD</span>
</div>

<div class="abs offer">
  <div class="ribbon">HOT DEAL</div>
  <div class="t">GET ULTIMATE<br>PC SUPPORT NOW!</div>
  <div class="price">JUST $99 <small>/ M</small></div>
  <div class="boxes" role="img" aria-label="Row of white software boxes"></div>
</div>

<section class="abs features"></section>
<article class="abs feature" style="left:120px">
  <div class="badge cond">A</div>
  <h4>SOLUTIONS</h4><div class="sub">A good idea to bring</div>
  <div class="dots">• • •</div>
  <p>We provide you with a comprehensive package of technical support services, for your computer, laptops, and other software peripherals.</p>
  <div class="more">READ MORE</div>
</article>
<article class="abs feature" style="left:301px">
  <div class="badge cond">B</div>
  <h4>VIRUS PROTECTION</h4><div class="sub">CleanGuard is the best here</div>
  <div class="dots">• • •</div>
  <p>Get unlimited tech support and effective virus removal security, diagnosis and repair of your pc issues all through the year.</p>
  <div class="more">READ MORE</div>
</article>
<article class="abs feature" style="left:481px">
  <div class="badge cond">C</div>
  <h4>MANAGE</h4><div class="sub">Enhanced PC's performance</div>
  <div class="dots">• • •</div>
  <p>Our optimization service involves removal of youras threats, unwanted files and unnecessary background processes.</p>
  <div class="more">READ MORE</div>
</article>

<h3 class="abs h-sec" style="left:124px;top:845px">OUR SERVICE PLAN</h3>
<div class="abs rule" style="left:124px;top:869px;width:250px"></div>
<h3 class="abs h-sec" style="left:397px;top:845px">WHAT WE DO</h3>
<div class="abs rule" style="left:397px;top:869px;width:247px"></div>

<div class="abs plan" style="left:127px;top:891px"><span class="n">1</span><span class="l">Instant<br>Plan</span></div>
<div class="abs plan" style="left:212px;top:891px"><span class="n">2</span><span class="l">Bronze<br>Plan</span></div>
<div class="abs plan" style="left:299px;top:891px"><span class="n">3</span><span class="l">Silver<br>Plan</span></div>
<div class="abs plan" style="left:127px;top:940px"><span class="n">4</span><span class="l">Gold<br>Plan</span></div>
<div class="abs plan" style="left:212px;top:940px"><span class="n">5</span><span class="l">Diamond<br>Plan</span></div>
<div class="abs plan" style="left:299px;top:940px"><span class="n">6</span><span class="l">Platinum<br>Plan</span></div>

<div class="abs whatwedo"></div>
<div class="abs wwd-photo" role="img" aria-label="Portrait of a support engineer in a suit"></div>
<p class="abs wwd-text">Solutions Premium Phone Tech Support is always ready to provide resolutions, 24x7x365. Speak Live to our Solution Engineers and get fast, precise resolution for your PC and other technical problems.</p>
<div class="abs wwd-more">MORE ▸</div>

<div class="abs footband">PC OPTIMIZE TOOL FOR&nbsp;<em>SUPPORT &amp; SPEED</em>&nbsp;UP YOUR PC</div>
<div class="abs callbox"></div>
<div class="abs call"><span class="c"></span><span class="c"></span>&nbsp;CALL: +1 555 010 2299</div>

<footer class="abs footer"></footer>
<h4 class="abs f-h" style="left:127px;top:1086px">NEVIGATION</h4>
<ul class="abs f-list" style="left:120px;top:1116px">
  <li>HOME</li><li>ABOUT US</li><li>SERVICE PLAN</li><li>CONTACT US</li>
</ul>
<h4 class="abs f-h" style="left:252px;top:1088px">OUR SERVICE</h4>
<ul class="abs f-list" style="left:245px;top:1116px">
  <li>INSTANT</li><li>ANTIVIRUS</li><li>GOLD</li><li>PLATINUM</li>
</ul>
<ul class="abs f-list" style="left:315px;top:1116px">
  <li>BRONZE</li><li>DIAMOND</li>
</ul>
<h4 class="abs f-h" style="left:433px;top:1086px;font-family:'Open Sans',sans-serif;font-size:9.5px">About Us</h4>
<p class="abs f-about">Solutions is a technical support service with operation centers that cover most of the major cities in the world. As computers have become more popular and sophisticated, the job of keeping them running has been taken known collectively as "Solution Engineers".</p>

</body>
</html>
```